Business card por a urban DJ, up scale audience target

Need a sober design, modern, conservative colors but i can consider some options, y play rnb, hip hop, EDM and top40.

Business card for contact and personal info, double sided, use logo attrached please; im 42 so i need a card acording to my age an target audience.

Target Market(s)

Adult people, up scale audience

Industry/Entity Type

Music Download

Contact Information for Business Card

Cel (318) 5024471963 www.kelvarodun.com

Requirements
Must have
• open mind
Nice to have
• open mind
Should not have
• DJ

```html
<!DOCTYPE html>
<html lang="en">
<head>
<meta charset="utf-8">
<title>Kelva business card</title>
<link rel="stylesheet" href="https://fonts.googleapis.com/css2?family=Questrial&display=swap">
<style>
  :root {
    --bg: #e9e7e3;
    --paper: #ffffff;
    --ink: #2b2b2b;
    --black: #111111;
    --light: #f4f4f4;
    --font: "Questrial", "Century Gothic", sans-serif;
  }
  * { margin: 0; padding: 0; box-sizing: border-box; }
  html, body { width: 1200px; height: 892px; overflow: hidden; }
  body {
    background: var(--bg);
    font-family: var(--font);
    display: flex;
    flex-direction: column;
    align-items: center;
    justify-content: center;
    gap: 60px;
  }
  .card {
    position: relative;
    width: 630px;
    height: 360px;
    background: var(--paper);
    box-shadow: 0 6px 18px rgba(0,0,0,.18);
    overflow: hidden;
  }

  /* wordmark */
  .wordmark {
    display: flex;
    align-items: center;
    gap: 14px;
    color: var(--ink);
  }
  .wordmark-square { width: 26px; height: 26px; background: var(--ink); }
  .wordmark-name { font-size: 96px; letter-spacing: 4px; line-height: 1; }

  /* back side */
  .card-back .wordmark {
    position: absolute;
    left: 50%; top: 92px;
    transform: translateX(-50%);
  }
  .card-back .site {
    position: absolute;
    left: 0; right: 0; top: 250px;
    display: flex;
    align-items: center;
    justify-content: center;
    gap: 16px;
    font-size: 22px;
    color: var(--ink);
  }
  .site-rule { width: 90px; height: 1px; background: var(--ink); }

  /* front side */
  .card-front .shape { position: absolute; inset: 0; }
  .card-front .wordmark {
    position: absolute;
    left: 210px; top: 34px;
  }
  .card-front .wordmark-name { font-size: 80px; }
  .holder {
    position: absolute;
    left: 26px; top: 190px;
    color: var(--light);
  }
  .holder-name { font-size: 30px; letter-spacing: .5px; }
  .holder-role { font-size: 20px; margin-top: 2px; }
  .contacts {
    position: absolute;
    left: 288px; top: 228px;
    padding-left: 16px;
    border-left: 1.5px solid var(--light);
    list-style: none;
    color: var(--light);
    font-size: 16px;
  }
  .contacts li {
    display: flex;
    align-items: center;
    gap: 10px;
    height: 25px;
  }
  .contacts svg { width: 14px; height: 14px; flex: none; }
</style>
</head>
<body>

  <section class="card card-back" aria-label="Card back">
    <div class="wordmark">
      <span class="wordmark-square"></span>
      <span class="wordmark-name">KELVA</span>
    </div>
    <div class="site">
      <span class="site-rule"></span>
      <span>www.kelvarodun.com</span>
      <span class="site-rule"></span>
    </div>
  </section>

  <section class="card card-front" aria-label="Card front">
    <svg class="shape" viewBox="0 0 630 360" preserveAspectRatio="none" aria-hidden="true">
      <polygon points="0,96 36,126 590,200 630,193 630,199 590,208 32,134 0,104" fill="var(--black)"/>
      <polygon points="0,116 30,146 592,222 630,214 630,360 0,360" fill="var(--ink)"/>
    </svg>

    <div class="wordmark">
      <span class="wordmark-square"></span>
      <span class="wordmark-name">KELVA</span>
    </div>

    <div class="holder">
      <p class="holder-name">Theo Brannick</p>
      <p class="holder-role">Managing Director</p>
    </div>

    <ul class="contacts">
      <li>
        <svg viewBox="0 0 14 14" aria-hidden="true"><rect width="14" height="14" rx="2" fill="var(--light)"/><path d="M4 3.5c-.8.6-.8 2 .4 3.8s2.7 3 3.7 3.1c.6 0 1-.3 1.4-.8l-1.5-1.4-.9.6c-.7-.3-1.7-1.4-2-2.1l.6-.9L4.4 3.3z" fill="var(--ink)"/></svg>
        <span>(318) 5024471963</span>
      </li>
      <li>
        <svg viewBox="0 0 14 14" aria-hidden="true"><rect width="14" height="14" rx="2" fill="var(--light)"/><rect x="2.5" y="4" width="9" height="6.5" fill="none" stroke="var(--ink)" stroke-width="1"/><path d="M2.5 4l4.5 3.6L11.5 4" fill="none" stroke="var(--ink)" stroke-width="1"/></svg>
        <span>info@kelvarodun.com</span>
      </li>
      <li>
        <svg viewBox="0 0 14 14" aria-hidden="true"><rect width="14" height="14" rx="2" fill="var(--light)"/><circle cx="7" cy="7" r="4.2" fill="none" stroke="var(--ink)" stroke-width="1"/><ellipse cx="7" cy="7" rx="1.8" ry="4.2" fill="none" stroke="var(--ink)" stroke-width="1"/><path d="M2.8 7h8.4" stroke="var(--ink)" stroke-width="1"/></svg>
        <span>www.kelvarodun.com</span>
      </li>
      <li>
        <svg viewBox="0 0 14 14" aria-hidden="true"><rect width="14" height="14" rx="2" fill="var(--light)"/><path d="M7 12S3.8 8.2 3.8 5.8a3.2 3.2 0 0 1 6.4 0C10.2 8.2 7 12 7 12z" fill="var(--ink)"/><circle cx="7" cy="5.8" r="1.2" fill="var(--light)"/></svg>
        <span>418 Marrow Lane, Dunmore PA 185</span>
      </li>
    </ul>
  </section>

</body>
</html>
```